make it look old timey and motherly but mordern...bath soak with cooling vapors. tall pine hush

need a bath soak label...cooling vapors. will be in a pouch like below. dont pay attention to the design, just attatching so you know the kind of pouch itll be in. need something trusty, minimal and clean...its called tall pine hush bath soak the best bath yull ever take.... for sore muscles, cooling vapors, smells good...made with menthol lemon and eucalyptus...give me something good.

Target Market(s)

make it look old timey and motherly but mordern

Font styles to use
Serif
Sans Serif

Colors
0054AA
0677BA
7BADD7
CADEEF
E8F1F8
0094D4
00A9DD
6FCCEA
C7EBF8
E9F6FB
FFF300
FFF600
FEFA6F
FFFEC7
FFFEE8
FFC000
F8CF3A
FAE287
FDF2CF
FEFAEE
E54698
E96AAD
F1A4CE
F9D9EA
FCEFF6
6B429C
8869AF
B7A5CE
E3DAEB
F3F0F8

```html
<!DOCTYPE html>
<html lang="en">
<head>
<meta charset="utf-8">
<title>Tall Pine Hush Bath Soak</title>
<link rel="stylesheet" href="https://fonts.googleapis.com/css2?family=Montserrat:wght@300;400;600&display=swap">
<style>
  :root {
    --stage: #f3f0f8;
    --violet-deep: #6b429c;
    --violet: #8869af;
    --violet-soft: #b7a5ce;
    --periwinkle: #8e9fcf;
    --blush: #e8a6a8;
    --rose: #e2918f;
    --pearl: #f1eef3;
    --ink-light: #ffffff;
    --ink-soft: rgba(255,255,255,0.82);
  }
  * { margin: 0; padding: 0; box-sizing: border-box; }
  html, body {
    width: 986px; height: 1200px; overflow: hidden;
    background: var(--stage);
    font-family: "Montserrat", sans-serif;
  }
  .canvas { position: relative; width: 986px; height: 1200px; }
  .pouch {
    position: absolute; left: 103px; top: 40px;
    width: 780px; height: 1120px;
    background:
      linear-gradient(20deg, var(--periwinkle) 0%, #a99cc8 35%, #d7a9bd 65%, var(--rose) 100%);
    overflow: hidden;
  }
  .pouch-top { position: absolute; left: 0; top: 0; width: 780px; height: 260px; }
  .seal-line {
    position: absolute; left: 0; right: 0; top: 140px; height: 2px;
    background: rgba(255,255,255,0.35);
  }
  .brand-ring {
    position: absolute; left: 183px; top: 372px;
    width: 414px; height: 414px;
    border: 2px solid var(--ink-light); border-radius: 50%;
  }
  .brand-name {
    position: absolute; left: 0; right: 0; top: 500px;
    text-align: center; color: var(--ink-light);
    font-weight: 300; font-size: 64px; line-height: 1.05;
    letter-spacing: 1px;
  }
  .product-type {
    position: absolute; left: 0; right: 0; top: 800px;
    text-align: center; color: var(--ink-light);
    font-weight: 600; font-size: 20px; letter-spacing: 3px;
  }
  .tagline {
    position: absolute; left: 0; right: 0; top: 830px;
    text-align: center; color: var(--ink-soft);
    font-weight: 300; font-size: 20px; letter-spacing: 4px;
  }
  .ingredients {
    position: absolute; left: 0; right: 0; top: 882px;
    display: flex; justify-content: center; gap: 30px;
  }
  .ingredient { width: 100px; text-align: center; }
  .ingredient-art {
    width: 62px; height: 62px; margin: 0 auto 14px;
    border-radius: 50%;
    background: rgba(255,255,255,0.28);
  }
  .ingredient-name {
    color: var(--ink-light); font-weight: 600; font-size: 14px; letter-spacing: 1px;
  }
  .base-band {
    position: absolute; left: 0; right: 0; top: 1022px; height: 12px;
    background: var(--violet);
  }
  .weight-band {
    position: absolute; left: 0; right: 0; top: 1044px; height: 38px;
    background: var(--violet-deep);
    color: var(--ink-light); text-align: center;
    font-weight: 600; font-size: 16px; line-height: 38px; letter-spacing: 1px;
  }
</style>
</head>
<body>
<main class="canvas">
  <section class="pouch">
    <svg class="pouch-top" viewBox="0 0 780 260" aria-hidden="true">
      <rect x="0" y="0" width="780" height="18" fill="#e4999c"/>
      <rect x="0" y="18" width="780" height="110" fill="#8c6cb1"/>
      <path d="M0 18 L0 260 L780 260 L780 18 C700 20 560 40 480 80 C440 100 410 120 390 138 C370 120 340 100 300 80 C220 40 80 20 0 18 Z" fill="var(--pearl)" opacity="0.92"/>
      <rect x="0" y="160" width="780" height="100" fill="url(#fade)"/>
      <defs>
        <linearGradient id="fade" x1="0" y1="0" x2="0" y2="1">
          <stop offset="0" stop-color="#f1eef3" stop-opacity="0"/>
          <stop offset="1" stop-color="#d9c7d6" stop-opacity="0.4"/>
        </linearGradient>
      </defs>
    </svg>
    <div class="seal-line"></div>

    <div class="brand-ring"></div>
    <h1 class="brand-name">tall pine<br>hush</h1>

    <p class="product-type">BATH SOAK</p>
    <p class="tagline">the best bath you'll ever take</p>

    <div class="ingredients">
      <div class="ingredient">
        <div class="ingredient-art" role="img" aria-label="line drawing of a mint leaf"></div>
        <span class="ingredient-name">menthol</span>
      </div>
      <div class="ingredient">
        <div class="ingredient-art" role="img" aria-label="line drawing of a lemon slice"></div>
        <span class="ingredient-name">lemon</span>
      </div>
      <div class="ingredient">
        <div class="ingredient-art" role="img" aria-label="line drawing of a eucalyptus sprig"></div>
        <span class="ingredient-name">eucalyptus</span>
      </div>
    </div>

    <div class="base-band"></div>
    <div class="weight-band">425 gram</div>
  </section>
</main>
</body>
</html>
```